PressNest Plugin Cover Image for ScriptHarbor

We need a new cover image for our PressNest plugin Mosaic Brick Pane Album, you can see it here: http://scriptharbor.example/item/mosaic-brick-pane-album-for-wordpress/7403628 the cover image is: http://2.cdn.quorvel.example/files/52917340/MBP_1.jpg this is a plugin to make galleries with a new concept grid, where images are tiled like a puzzle, instead of the usual multi-columns or multi-rows layouts. See details here: http://belstrandia.example/mosaic-brick-album-demo

The cover image has to communicate few key features of the plugin and it should show an example of the galleries the user can create.

The main feature is the completely new and unique grid system.

You are free and encouraged to use new colors and fonts, I like high contrast schemes like dark grey and fluo colors (orange, lime, cyan).

This is a list of other cover images I like the style:
http://0.cdn.quorvel.example/files/61204758/01_Preview.jpg
http://3.cdn.quorvel.example/files/48830512/Banner.png
http://1.cdn.quorvel.example/files/27749065/image-preview.png
http://0.cdn.quorvel.example/files/93156207/previewv12.jpg
http://1.cdn.quorvel.example/files/16628473/preview.jpg

```html
<!DOCTYPE html>
<html lang="en">
<head>
<meta charset="utf-8">
<title>Mosaic Brick Pane Album – Plugin Cover</title>
<link rel="stylesheet" href="https://fonts.googleapis.com/css2?family=Lato:wght@300;400;700;900&display=swap">
<style>
  :root {
    --bg-center: #3b3b3d;
    --bg-edge: #161617;
    --white: #ffffff;
    --accent-green: #4fe07d;
    --strip-teal: #19cfa0;
    --strip-green: #4fdc63;
    --strip-lime: #c9e82a;
    --strip-orange: #f5882b;
    --strip-pink: #f0336a;
    --bar-pink: #ef3368;
    --device-dark: #1b1b1d;
    --device-silver: #d9dadc;
    --gallery-bg: #f2f2f2;
    --tone-stone: #9fa5a6;
    --tone-sky: #c7cccd;
    --tone-brick: #7a4a36;
    --tone-night: #2c2a2e;
    --tone-green: #5d7550;
    --tone-blue: #5b7fa8;
    --tone-sand: #b29a78;
    --tone-rust: #a4552e;
    --tone-slate: #6f787d;
  }
  * { margin: 0; padding: 0; box-sizing: border-box; }
  html, body { width: 1200px; height: 610px; overflow: hidden; }
  body { font-family: "Lato", sans-serif; color: var(--white); background: var(--bg-edge); }

  .cover {
    position: relative; width: 1200px; height: 610px; overflow: hidden;
    background: radial-gradient(ellipse 70% 80% at 50% 40%, var(--bg-center) 0%, #262628 55%, var(--bg-edge) 100%);
  }

  .color-strip { position: absolute; top: 0; left: 0; width: 100%; height: 28px; display: flex; }
  .color-strip span { flex: 1; }
  .color-strip .teal { background: var(--strip-teal); }
  .color-strip .green { background: var(--strip-green); }
  .color-strip .lime { background: var(--strip-lime); }
  .color-strip .orange { background: var(--strip-orange); }
  .color-strip .pink { background: var(--strip-pink); }

  .title { position: absolute; left: 78px; top: 62px; text-transform: uppercase; line-height: 1; }
  .title-main { display: block; font-weight: 900; font-size: 74px; letter-spacing: 1px; }
  .title-sub { display: block; font-weight: 300; font-size: 68px; letter-spacing: 9px; margin-top: 4px; }

  .features { position: absolute; left: 34px; top: 214px; list-style: none; font-size: 31px; line-height: 54px; white-space: nowrap; }
  .features strong { color: var(--accent-green); font-weight: 700; }

  .platform-badge { position: absolute; top: 68px; right: 64px; display: flex; align-items: center; gap: 12px; font-weight: 700; font-size: 20px; }
  .platform-badge .dot { width: 44px; height: 44px; border-radius: 50%; background: var(--white); }

  .device { position: absolute; background: var(--device-dark); }
  .screen {
    position: absolute; display: grid; gap: 3px; padding: 3px;
    background: var(--gallery-bg);
  }
  .tile { display: block; }
  .stone { background: linear-gradient(180deg, var(--tone-sky), var(--tone-stone)); }
  .brick { background: var(--tone-brick); }
  .night { background: var(--tone-night); }
  .green { background: var(--tone-green); }
  .blue { background: var(--tone-blue); }
  .sand { background: var(--tone-sand); }
  .rust { background: var(--tone-rust); }
  .slate { background: var(--tone-slate); }

  .device-monitor {
    left: 708px; top: 168px; width: 452px; height: 356px; border-radius: 10px;
    background: linear-gradient(180deg, var(--device-dark) 0 86%, var(--device-silver) 86% 100%);
  }
  .device-monitor .screen {
    left: 28px; top: 19px; right: 28px; bottom: 52px;
    grid-template-columns: repeat(8, 1fr); grid-template-rows: repeat(6, 1fr);
  }
  .monitor-stand { position: absolute; left: 900px; top: 524px; width: 90px; height: 30px; background: linear-gradient(180deg, #b9babd, #8e8f92); }

  .device-tablet { left: 668px; top: 274px; width: 218px; height: 278px; border-radius: 16px; }
  .device-tablet .screen {
    left: 16px; top: 26px; right: 16px; bottom: 26px;
    grid-template-columns: repeat(4, 1fr); grid-template-rows: repeat(6, 1fr);
  }

  .device-phone { left: 866px; top: 374px; width: 66px; height: 178px; border-radius: 14px; }
  .device-phone .screen {
    left: 5px; top: 30px; right: 5px; bottom: 30px;
    grid-template-columns: repeat(2, 1fr); grid-template-rows: repeat(4, 1fr); gap: 2px; padding: 2px;
  }

  .support-bar {
    position: absolute; left: 540px; bottom: 0; width: 660px; height: 66px;
    background: var(--bar-pink); display: flex; align-items: center; justify-content: flex-end; gap: 54px; padding-right: 40px;
  }
  .support-bar .mark { width: 38px; height: 38px; border-radius: 50%; background: var(--white); }
</style>
</head>
<body>
<main class="cover">
  <div class="color-strip" aria-hidden="true">
    <span class="teal"></span><span class="green"></span><span class="lime"></span><span class="orange"></span><span class="pink"></span>
  </div>

  <h1 class="title">
    <span class="title-main">Mosaic Brick</span>
    <span class="title-sub">Pane Album</span>
  </h1>

  <ul class="features">
    <li><strong>&gt; Complex grids</strong> (no rows, squares or columns)</li>
    <li><strong>&gt; Responsive</strong> / Mobile layout</li>
    <li><strong>&gt; 5 lightboxes</strong> included</li>
    <li><strong>&gt; Custom links</strong> on images</li>
    <li><strong>&gt; Advanced admin</strong> UI</li>
    <li><strong>&gt; Fine tuning</strong> on captions</li>
  </ul>

  <div class="platform-badge"><span>PressNest</span><span class="dot"></span></div>

  <div class="device device-monitor">
    <div class="screen" role="img" aria-label="Tiled gallery of city photos led by a large domed government building">
      <span class="tile brick" style="grid-column:1/3;grid-row:1/3"></span>
      <span class="tile stone" style="grid-column:3/9;grid-row:1/6"></span>
      <span class="tile night" style="grid-column:1/3;grid-row:3/5"></span>
      <span class="tile slate" style="grid-column:1/3;grid-row:5/7"></span>
      <span class="tile green" style="grid-column:3/6;grid-row:6/7"></span>
      <span class="tile sand" style="grid-column:6/9;grid-row:6/7"></span>
    </div>
  </div>
  <div class="monitor-stand" aria-hidden="true"></div>

  <div class="device device-tablet">
    <div class="screen" role="img" aria-label="Mosaic gallery of city street and landmark photos">
      <span class="tile rust" style="grid-column:1/3;grid-row:1/3"></span>
      <span class="tile night" style="grid-column:3/5;grid-row:1/2"></span>
      <span class="tile slate" style="grid-column:3/4;grid-row:2/4"></span>
      <span class="tile brick" style="grid-column:4/5;grid-row:2/3"></span>
      <span class="tile blue" style="grid-column:1/2;grid-row:3/5"></span>
      <span class="tile stone" style="grid-column:2/3;grid-row:3/6"></span>
      <span class="tile sand" style="grid-column:4/5;grid-row:3/5"></span>
      <span class="tile green" style="grid-column:3/4;grid-row:4/6"></span>
      <span class="tile night" style="grid-column:1/2;grid-row:5/7"></span>
      <span class="tile blue" style="grid-column:4/5;grid-row:5/7"></span>
      <span class="tile green" style="grid-column:2/4;grid-row:6/7"></span>
    </div>
  </div>

  <div class="device device-phone">
    <div class="screen" role="img" aria-label="Mosaic gallery of city photos on a phone">
      <span class="tile blue" style="grid-column:1/3;grid-row:1/2"></span>
      <span class="tile brick" style="grid-column:1/2;grid-row:2/4"></span>
      <span class="tile stone" style="grid-column:2/3;grid-row:2/3"></span>
      <span class="tile green" style="grid-column:2/3;grid-row:3/5"></span>
      <span class="tile sand" style="grid-column:1/2;grid-row:4/5"></span>
    </div>
  </div>

  <div class="support-bar" aria-label="Supported browsers and platforms">
    <span class="mark"></span><span class="mark"></span><span class="mark"></span><span class="mark"></span><span class="mark"></span><span class="mark"></span><span class="mark"></span>
  </div>
</main>
</body>
</html>
```